QK active wear

Hey There

QK is a brand new QK Sydney base company. our clothe design by professional dancers & athletics. pushing the niche market of QK. the products we have is cool fashionable functional Eco friendly!!!

it caters male and female. who stays active and wants to be chic at the same time.
we would like to be associate with B-8 & Harbor threads & Vorn kind of brands.

i need you guys to use the existing logo to restructure it. turn it into consistent format that can be shared through out all the electronic business stationery. pls refer to all the photos i have upload in this brief. hopefully it'll gives you guys more of what i like i needs to be done.

PS: business card material specifications needs to be provided.
just so send the details to the printing company without explain too much.

Cheers

Industry/Entity Type

Electronic

Requirements
Must have
• It needs be more readable. clean. current. pop. fashionable.
interesting details across the broad for all electronic stationary.

for you to think about it and working on : company's business letters, order forms, its notices and other official publications, promissory notes, endorsements, cheques and orders for money or goods purporting to be signed by, or on behalf of, the company invoices, receipts websites

```html
<!DOCTYPE html>
<html lang="en">
<head>
<meta charset="utf-8">
<title>QK – Business Card Options</title>
<link rel="stylesheet" href="https://fonts.googleapis.com/css2?family=Montserrat:wght@400;500&family=Open+Sans:wght@400&display=swap">
<style>
  :root {
    --board: #414241;
    --card-black: #0f1110;
    --card-deep: #040607;
    --paper: #ffffff;
    --teal: #1b8a7a;
    --teal-bright: #20a89a;
    --ink: #111111;
    --white: #ffffff;
    --muted: #8c8c8c;
    --stone: #6a6a6a;
    --label: #b4b4b4;
  }
  * { margin: 0; padding: 0; box-sizing: border-box; }
  html, body { width: 1200px; height: 1000px; overflow: hidden; background: var(--board); }
  body { position: relative; font-family: "Montserrat", sans-serif; }

  .card { position: absolute; width: 488px; height: 279px; overflow: hidden; }
  .card--one { left: 100px; top: 97px; background: var(--card-black); }
  .card--two { left: 641px; top: 97px; background: var(--paper); }
  .card--three { left: 100px; top: 546px; background: var(--paper); }
  .card--four { left: 641px; top: 546px; background: var(--paper); }

  .panel-dark { position: absolute; left: 0; top: 0; background: var(--card-deep); }
  .card--two .panel-dark { width: 259px; height: 279px; }
  .card--three .panel-dark, .card--four .panel-dark { width: 488px; height: 183px; }

  .brand-mark { position: absolute; background: var(--teal); }
  .brand { position: absolute; font-weight: 500; line-height: 1; white-space: nowrap; color: var(--white); letter-spacing: 2px; }

  .card--one .brand-mark, .card--two .brand-mark { left: 96px; top: 36px; width: 70px; height: 70px; }
  .card--one .brand, .card--two .brand { left: 0; width: 262px; top: 128px; text-align: center; font-size: 88px; }
  .card--two .brand { width: 259px; }

  .card--three .brand-mark { left: 100px; top: 38px; width: 96px; height: 96px; }
  .card--three .brand { left: 220px; top: 40px; font-size: 92px; }
  .card--four .brand-mark { left: 110px; top: 42px; width: 88px; height: 88px; background: var(--teal-bright); }
  .card--four .brand { left: 222px; top: 42px; font-size: 88px; color: var(--stone); }

  .tagline { position: absolute; font-size: 10px; color: var(--muted); letter-spacing: 0.2px; white-space: nowrap; }
  .card--one .tagline, .card--two .tagline { left: 0; width: 262px; text-align: center; top: 231px; }
  .card--two .tagline { width: 259px; }
  .card--three .tagline { left: 224px; top: 136px; }
  .card--four .tagline { left: 224px; top: 142px; }

  .person { position: absolute; }
  .person-name { font-size: 21px; font-weight: 400; letter-spacing: 0.3px; line-height: 1; }
  .person-role { font-family: "Open Sans", sans-serif; font-size: 13px; margin-top: 6px; line-height: 1; }
  .card--one .person { left: 301px; top: 33px; color: var(--white); }
  .card--two .person { left: 300px; top: 33px; color: var(--ink); }
  .card--three .person, .card--four .person { left: 52px; top: 209px; color: var(--ink); }
  .card--two .person-name, .card--three .person-name, .card--four .person-name { color: var(--teal); }

  .contact { position: absolute; list-style: none; font-family: "Open Sans", sans-serif; font-size: 13px; line-height: 16px; }
  .contact li { display: flex; align-items: center; gap: 5px; white-space: nowrap; }
  .contact svg { width: 10px; height: 10px; flex: none; }
  .card--one .contact { left: 299px; top: 195px; color: var(--white); }
  .card--two .contact { left: 299px; top: 195px; color: var(--ink); }
  .card--three .contact, .card--four .contact { left: 290px; top: 202px; color: var(--ink); }
  .card--two .contact svg, .card--three .contact svg, .card--four .contact svg { color: var(--teal); }

  .option-label { position: absolute; width: 488px; text-align: center; font-family: "Open Sans", sans-serif; font-size: 22px; color: var(--label); letter-spacing: 0.5px; }
</style>
</head>
<body>
<svg width="0" height="0" style="position:absolute" aria-hidden="true">
  <defs>
    <symbol id="icon-phone" viewBox="0 0 10 10"><path d="M3 0.5 L4.2 2.8 L3.3 3.8 C3.8 5 4.8 6 6 6.6 L7 5.6 L9.4 6.8 L8.6 9 C4.5 9 0.9 5.4 1 1.3 Z" fill="currentColor"/></symbol>
    <symbol id="icon-mail" viewBox="0 0 10 10"><rect x="0.5" y="2" width="9" height="6.5" fill="none" stroke="currentColor" stroke-width="1"/><path d="M0.8 2.3 L5 5.6 L9.2 2.3" fill="none" stroke="currentColor" stroke-width="1"/></symbol>
    <symbol id="icon-web" viewBox="0 0 10 10"><g fill="none" stroke="currentColor" stroke-width="1"><circle cx="5" cy="5" r="4.3"/><ellipse cx="5" cy="5" rx="1.9" ry="4.3"/><path d="M0.7 5 H9.3 M1.5 2.8 H8.5 M1.5 7.2 H8.5"/></g></symbol>
  </defs>
</svg>

<section class="card card--one">
  <div class="brand-mark"></div>
  <p class="brand">QK</p>
  <p class="tagline">MOVE FREE STAY TRUE TO YOU</p>
  <div class="person"><p class="person-name">MARCUS LEE</p><p class="person-role">Managing Director</p></div>
  <ul class="contact">
    <li><svg><use href="#icon-phone"/></svg>0-000-000-0000</li>
    <li><svg><use href="#icon-mail"/></svg>marcus@qkwear.com</li>
    <li><svg><use href="#icon-web"/></svg>www.qkwear.com</li>
  </ul>
</section>
<p class="option-label" style="left:100px; top:430px;">OPTION 1</p>

<section class="card card--two">
  <div class="panel-dark"></div>
  <div class="brand-mark"></div>
  <p class="brand">QK</p>
  <p class="tagline">MOVE FREE STAY TRUE TO YOU</p>
  <div class="person"><p class="person-name">MARCUS LEE</p><p class="person-role">Managing Director</p></div>
  <ul class="contact">
    <li><svg><use href="#icon-phone"/></svg>0-000-000-0000</li>
    <li><svg><use href="#icon-mail"/></svg>marcus@qkwear.com</li>
    <li><svg><use href="#icon-web"/></svg>www.qkwear.com</li>
  </ul>
</section>
<p class="option-label" style="left:641px; top:430px;">OPTION 2</p>

<section class="card card--three">
  <div class="panel-dark"></div>
  <div class="brand-mark"></div>
  <p class="brand">QK</p>
  <p class="tagline">MOVE FREE STAY TRUE TO YOU</p>
  <div class="person"><p class="person-name">MARCUS LEE</p><p class="person-role">Managing Director</p></div>
  <ul class="contact">
    <li><svg><use href="#icon-phone"/></svg>0-000-000-0000</li>
    <li><svg><use href="#icon-mail"/></svg>marcus@qkwear.com</li>
    <li><svg><use href="#icon-web"/></svg>www.qkwear.com</li>
  </ul>
</section>
<p class="option-label" style="left:100px; top:880px;">OPTION 3</p>

<section class="card card--four">
  <div class="panel-dark"></div>
  <div class="brand-mark"></div>
  <p class="brand">QK</p>
  <p class="tagline">MOVE FREE STAY TRUE TO YOU</p>
  <div class="person"><p class="person-name">MARCUS LEE</p><p class="person-role">Managing Director</p></div>
  <ul class="contact">
    <li><svg><use href="#icon-phone"/></svg>0-000-000-0000</li>
    <li><svg><use href="#icon-mail"/></svg>marcus@qkwear.com</li>
    <li><svg><use href="#icon-web"/></svg>www.qkwear.com</li>
  </ul>
</section>
<p class="option-label" style="left:641px; top:880px;">OPTION 4</p>
</body>
</html>
```